依頼概要
■依頼の目的/概要
インフルエンザワクチンのポスターを作成して頂きたいです。
クリニック内の待合室に掲示します。

■依頼詳細
A2サイズです。
温かみのある柔らかいデザインをお願いします。
ポスターには、人のイラスト入りでお願いします。イラストはご自身で書いてくださってもいいですし、フリー素材でも構いません。
色合いは当院ホームページを参考にしてください。
当院ホームページ https://temuzeku.com/

記載する内容については、添付ファイルを参照してください。
ロゴデータは当選決定後に送らせて頂きます。

納品は、元データ(aiファイルやpsdファイル)とPNG書き出しでお願いします。

■重視する点
過去・現在までにデザインの経験のある方を希望致します。

その他何かご不明な点がございましたら、お気軽にご質問下さい。
よろしくお願いいたします。

文字が大きく読みやすい、温かみのあるデザインです。

皆さま、この度は当コンペにご参加いただき、誠にありがとうございます。
どれも力作で魅力的で選ぶのが大変でした。
今後ともどうぞよろしくお願いします。

```html
<!DOCTYPE html>
<html lang="ja">
<head>
<meta charset="utf-8">
<title>インフルエンザ予防接種</title>
<link rel="stylesheet" href="https://fonts.googleapis.com/css2?family=M+PLUS+Rounded+1c:wght@500;700;800&display=swap">
<style>
  :root {
    --bg: #fdf4e4;
    --orange: #f08a24;
    --orange-soft: #fbd9b0;
    --green: #4f9a3c;
    --green-soft: #dcefc9;
    --pink: #f29aa3;
    --pink-deep: #d9606c;
    --text: #4a3a2c;
    --white: #ffffff;
  }
  * { margin: 0; padding: 0; box-sizing: border-box; }
  html, body { width: 849px; height: 1200px; overflow: hidden; background: var(--bg); }
  body { font-family: "M PLUS Rounded 1c", sans-serif; color: var(--text); }
  .poster { position: relative; width: 849px; height: 1200px; overflow: hidden;
    background: linear-gradient(#fff8ec, var(--bg)); }

  .family-art { position: absolute; left: 170px; top: 116px; width: 635px; height: 268px;
    border-radius: 130px 130px 24px 24px;
    background: linear-gradient(180deg, #fde4c4, #f7c7a0); }

  .title { position: absolute; top: 18px; left: 0; width: 100%; text-align: center; z-index: 2;
    font-size: 60px; line-height: 80px; font-weight: 800; color: var(--orange); letter-spacing: 2px;
    white-space: nowrap;
    text-shadow: 0 3px 0 #fff, 3px 0 0 #fff, -3px 0 0 #fff, 0 -3px 0 #fff; }

  .start-badge { position: absolute; left: 22px; top: 108px; width: 118px; height: 118px; z-index: 2;
    border-radius: 50%; background: var(--white); border: 4px solid var(--pink);
    display: flex; flex-direction: column; align-items: center; justify-content: center;
    color: var(--pink-deep); font-weight: 800; line-height: 1.25; white-space: nowrap; text-align: center; }
  .start-badge .date { font-size: 17px; }
  .start-badge .date small { font-size: 10px; }
  .start-badge .from { font-size: 12px; }
  .start-badge .begin { font-size: 17px; }

  .no-reservation { position: absolute; left: 30px; top: 244px; width: 104px; height: 38px;
    background: var(--pink); color: var(--white); border-radius: 19px; font-weight: 800;
    font-size: 18px; display: flex; align-items: center; justify-content: center; white-space: nowrap; }

  .fee-card { position: absolute; left: 48px; width: 753px; background: var(--white);
    border: 4px solid var(--orange); border-radius: 18px; display: flex; }
  .fee-card.subsidized { top: 405px; height: 262px; }
  .fee-card.general { top: 680px; height: 188px; }
  .who { width: 350px; padding: 34px 22px 0 30px; border-right: 3px dashed var(--orange-soft); }
  .who .group { font-size: 25px; font-weight: 800; line-height: 1.55; white-space: nowrap; }
  .who .note { font-size: 15px; font-weight: 500; line-height: 1.6; padding-left: 40px; }
  .terms { flex: 1; padding: 22px 20px 0 26px; }
  .terms .subsidy { font-size: 21px; font-weight: 800; color: var(--orange); margin-bottom: 8px; }
  .term-row { display: flex; align-items: flex-start; margin-bottom: 8px; font-size: 20px; font-weight: 700; }
  .term-label { flex: none; width: 104px; height: 30px; background: var(--orange); color: var(--white);
    font-size: 16px; border-radius: 4px; display: flex; align-items: center; justify-content: center;
    margin-right: 14px; }
  .term-row .value { line-height: 1.5; }
  .terms .remark { font-size: 16px; font-weight: 500; margin-top: 4px; }

  .notices { position: absolute; left: 60px; top: 885px; width: 741px; height: 188px;
    background: var(--white); border-radius: 16px; padding: 16px 22px; list-style: none;
    color: var(--green); font-size: 18px; font-weight: 700; line-height: 1.5; }
  .notices li { position: relative; padding-left: 28px; }
  .notices li::before { content: ""; position: absolute; left: 0; top: 7px; width: 16px; height: 16px;
    border-radius: 50%; background: var(--green); }

  .town-art { position: absolute; left: 0; top: 1075px; width: 849px; height: 125px;
    background: linear-gradient(180deg, var(--bg), var(--green-soft)); }

  .clinic { position: absolute; left: 0; top: 1128px; width: 100%; text-align: center; }
  .clinic .departments { font-size: 12px; color: var(--green); font-weight: 500; }
  .clinic .name { display: inline-flex; align-items: center; gap: 10px; font-size: 32px;
    font-weight: 800; color: var(--green); }
  .clinic .name .dot { width: 24px; height: 24px; border-radius: 50%; background: var(--green); }
</style>
</head>
<body>
<main class="poster">
  <div class="family-art" role="img" aria-label="笑顔の家族(祖父母・両親・子ども)のイラスト"></div>

  <h1 class="title">インフルエンザ予防接種</h1>

  <div class="start-badge">
    <span class="date">10月1日<small>(金)</small></span>
    <span class="from">から</span>
    <span class="begin">始まります</span>
  </div>
  <div class="no-reservation">予約不要</div>

  <section class="fee-card subsidized">
    <div class="who">
      <p class="group">・65歳以上</p>
      <p class="group">・60歳以上65歳未満</p>
      <p class="note">心臓・腎臓・肺に障害がある方(※)<br>HIV感染により免疫不全<br>※詳しくは医師にお尋ねください</p>
    </div>
    <div class="terms">
      <p class="subsidy">相模原市公費負担あり</p>
      <div class="term-row"><span class="term-label">接種費用</span><span class="value">¥1,500</span></div>
      <div class="term-row"><span class="term-label">接種回数</span><span class="value">1回</span></div>
      <div class="term-row"><span class="term-label">期間</span><span class="value">10/1～12/31</span></div>
      <p class="remark">・費用が免除になる方がいらっしゃいます</p>
    </div>
  </section>

  <section class="fee-card general">
    <div class="who">
      <p class="group">・上記以外の方</p>
      <p class="group">&nbsp;&nbsp;13歳以上65歳未満</p>
    </div>
    <div class="terms">
      <div class="term-row"><span class="term-label">接種費用</span><span class="value">(1回目)¥4,000<br>(2回目)¥3,000</span></div>
      <div class="term-row"><span class="term-label">接種回数</span><span class="value">1回もしくは2回</span></div>
      <div class="term-row"><span class="term-label">期間</span><span class="value">10/1～</span></div>
    </div>
  </section>

  <ul class="notices">
    <li>インフルエンザに対する抵抗力がつくまで約2週間かかり、<br>その効果は約5ヶ月続きます。</li>
    <li>2回接種をご希望の方は、1回目接種から4週間後に2回目接種を行います。</li>
    <li>肺炎球菌ワクチンとの同時接種はできます。</li>
    <li>体温が37.5度以上、具合が悪い方は別の日に接種しましょう。</li>
    <li>当院では妊娠中の方も予防接種できます。</li>
  </ul>

  <div class="town-art" role="img" aria-label="木々と家が並ぶ町並みのイラスト"></div>

  <footer class="clinic">
    <p class="departments">内科・呼吸器内科・消化器内科</p>
    <p class="name"><span class="dot"></span>青葉内科クリニック</p>
  </footer>
</main>
</body>
</html>
```